Screenshot Design for Quell App Store for business application

I will need 5 screenshots of my application "Slidewell Harbor" for the peview page for the Norvo Quell Store.

Screenshot requirements are:
One of the following sizes:
2560 x 1600 pixels
2880 x 1800 pixel

I will provide the following resources. Please feel free to take what you think is the best for the preview (any picture, logo, text line of all the files here). At the end, you only need 5 pictures and 5 text points, each for every screenshot.

- Logo files
- PDF preview of the DeckForge slide (please let me know if you need any special slide as PNG, it is too much data to add all PNGs)
- App Screenshot (you can change the picture with one from the pdfs)
- Example texts
- Colors: Blue #3083E8, Dark blue #1F1FB5, Yellow #F0C25D

My application offers business DeckForge templates and the screenshots should not only show the application itself, but some preview slides of the DeckForge templates. In case you have any question, please let me know.
Updates

Target Market(s)

Business people

Industry/Entity Type

Business

Font styles to use
Sans Serif

Requirements
Must have
• - One screenshot should show the application screenshot
• - Please use only the following colors: Blue #3083E8, Dark blue #1F1FB5, Yellow #F0C25D
• - Please look at other pictures of the Quell Appstore (https://shelf.quellmarket-example.com/us/genre/quell/id84?mt=57) and adapt your design to those
Nice to have
• - The blue as background would be preferred

```html
<!DOCTYPE html>
<html lang="en">
<head>
<meta charset="utf-8">
<title>Eight Color Schemes</title>
<link href="https://fonts.googleapis.com/css2?family=Rokkitt:wght@400;500&family=Open+Sans:wght@400;700&display=swap" rel="stylesheet">
<style>
  :root {
    --bg-glow: #07b0f2;
    --bg-mid: #0a5cb8;
    --bg-deep: #06307a;
    --band-top: #f4cf55;
    --band-mid: #ffeb8f;
    --band-bottom: #e6b448;
    --ink: #141414;
    --card: #ffffff;
    --grid: #d9d9d9;
    --label-text: #ffffff;
  }
  * { margin: 0; padding: 0; box-sizing: border-box; }
  html, body { width: 1200px; height: 750px; overflow: hidden; }
  body {
    position: relative;
    background: radial-gradient(ellipse 70% 75% at 50% 0%, var(--bg-glow) 0%, var(--bg-mid) 45%, var(--bg-deep) 100%);
    font-family: "Open Sans", sans-serif;
  }
  .headline-band {
    position: absolute; left: 0; top: 32px; width: 1200px; height: 54px;
    background: linear-gradient(to bottom, var(--band-top) 0%, var(--band-mid) 50%, var(--band-bottom) 100%);
    display: flex; align-items: center; justify-content: center;
  }
  .headline {
    font-family: "Rokkitt", serif; font-weight: 500; font-size: 36px;
    color: var(--ink); letter-spacing: 1.5px;
  }
  .scheme { position: absolute; width: 171px; }
  .scheme-card {
    width: 171px; height: 219px; background: var(--card); display: block;
    box-shadow: 0 6px 10px rgba(0, 20, 60, 0.35);
  }
  .scheme-name {
    margin-top: 19px; height: 24px; background: var(--label);
    color: var(--label-text); font-family: "Rokkitt", serif; font-size: 17px;
    letter-spacing: 1px; display: flex; align-items: center; justify-content: center;
  }
  .row-top { top: 141px; }
  .row-bottom { top: 440px; }
  .col-1 { left: 133px; } .col-2 { left: 370px; } .col-3 { left: 606px; } .col-4 { left: 838px; }

  .dark-blue { --dark: #121d62; --light: #5b84e8; --label: #141741; }
  .brown     { --dark: #4a2a20; --light: #d49a85; --label: #4a2a20; }
  .blue      { --dark: #163a5a; --light: #5d9bd6; --label: #163a5a; }
  .sea-green { --dark: #1e4a3a; --light: #7cc4b3; --label: #1f4a3b; }
  .grey      { --dark: #3a3f3d; --light: #a6aba8; --label: #333837; }
  .red       { --dark: #6a0a20; --light: #e9557a; --label: #6a0020; }
  .green     { --dark: #1f4a1f; --light: #78c27a; --label: #1f4a1f; }
  .orange    { --dark: #5a2a10; --light: #ee8f5a; --label: #f0821c; }

  .bar-title { fill: var(--dark); }
  .bar-title-text { fill: #fff; font-size: 6.5px; font-weight: 700; letter-spacing: 1px; }
  .bar-title-small { font-size: 5px; font-weight: 400; letter-spacing: 0; }
  .grid-line { stroke: var(--grid); stroke-width: 0.6; stroke-dasharray: 2 1.5; }
  .axis { stroke: #bbb; stroke-width: 0.6; }
  .tick { fill: var(--dark); font-size: 5px; }
  .cat { fill: var(--dark); font-size: 5px; text-anchor: middle; }
  .line-dark { fill: none; stroke: var(--dark); stroke-width: 1.4; }
  .line-light { fill: none; stroke: var(--light); stroke-width: 1.4; }
  .col-light { fill: var(--light); }
  .col-dark { fill: var(--dark); }
</style>
</head>
<body>

<svg width="0" height="0" style="position:absolute" aria-hidden="true">
  <defs>
    <symbol id="scheme-sheet" viewBox="0 0 214 274">
      <!-- line chart -->
      <rect class="bar-title" x="7" y="10" width="198" height="14"/>
      <text class="bar-title-text" x="106" y="19.5" text-anchor="middle">Title <tspan class="bar-title-small">(Text)</tspan></text>
      <line class="grid-line" x1="18" y1="31" x2="205" y2="31"/>
      <line class="grid-line" x1="18" y1="48" x2="205" y2="48"/>
      <line class="grid-line" x1="18" y1="65" x2="205" y2="65"/>
      <line class="grid-line" x1="18" y1="82" x2="205" y2="82"/>
      <line class="grid-line" x1="18" y1="99" x2="205" y2="99"/>
      <line class="axis" x1="18" y1="116" x2="205" y2="116"/>
      <text class="tick" x="7" y="33">50</text><text class="tick" x="7" y="50">40</text>
      <text class="tick" x="7" y="67">30</text><text class="tick" x="7" y="84">20</text>
      <text class="tick" x="7" y="101">10</text><text class="tick" x="10" y="118">0</text>
      <polyline class="line-light" points="28,76.9 43,73.5 58,68.4 74,76.9 89,80.3 105,83.7 120,73.5 135,76.9 151,80.3 166,83.7 182,73.5 197,76.9"/>
      <polyline class="line-dark" points="28,44.6 43,75.2 58,82 74,75.2 89,73.5 105,70.1 120,78.6 135,87.1 151,78.6 166,80.3 182,66.7 197,70.1"/>
      <g>
        <text class="cat" x="28" y="124">Text</text><text class="cat" x="43" y="124">Text</text>
        <text class="cat" x="58" y="124">Text</text><text class="cat" x="74" y="124">Text</text>
        <text class="cat" x="89" y="124">Text</text><text class="cat" x="105" y="124">Text</text>
        <text class="cat" x="120" y="124">Text</text><text class="cat" x="135" y="124">Text</text>
        <text class="cat" x="151" y="124">Text</text><text class="cat" x="166" y="124">Text</text>
        <text class="cat" x="182" y="124">Text</text><text class="cat" x="197" y="124">Text</text>
      </g>

      <!-- column chart -->
      <rect class="bar-title" x="7" y="143" width="198" height="14"/>
      <text class="bar-title-text" x="106" y="152.5" text-anchor="middle">Title <tspan class="bar-title-small">(Text)</tspan></text>
      <line class="grid-line" x1="18" y1="164" x2="205" y2="164"/>
      <line class="grid-line" x1="18" y1="178" x2="205" y2="178"/>
      <line class="grid-line" x1="18" y1="192" x2="205" y2="192"/>
      <line class="grid-line" x1="18" y1="206" x2="205" y2="206"/>
      <line class="grid-line" x1="18" y1="220" x2="205" y2="220"/>
      <line class="grid-line" x1="18" y1="234" x2="205" y2="234"/>
      <line class="axis" x1="18" y1="248" x2="205" y2="248"/>
      <text class="tick" x="7" y="166">60</text><text class="tick" x="7" y="180">50</text>
      <text class="tick" x="7" y="194">40</text><text class="tick" x="7" y="208">30</text>
      <text class="tick" x="7" y="222">20</text><text class="tick" x="7" y="236">10</text>
      <text class="tick" x="10" y="250">0</text>
      <g>
        <rect class="col-light" x="23" y="203.2" width="9" height="44.8"/>
        <rect class="col-light" x="38" y="197.6" width="9" height="50.4"/>
        <rect class="col-light" x="53" y="173.8" width="9" height="74.2"/>
        <rect class="col-light" x="69" y="173.8" width="9" height="74.2"/>
        <rect class="col-light" x="84" y="185" width="9" height="63"/>
        <rect class="col-light" x="100" y="200.4" width="9" height="47.6"/>
        <rect class="col-light" x="115" y="183.6" width="9" height="64.4"/>
        <rect class="col-light" x="130" y="180.8" width="9" height="67.2"/>
        <rect class="col-light" x="146" y="185" width="9" height="63"/>
        <rect class="col-light" x="161" y="200.4" width="9" height="47.6"/>
        <rect class="col-light" x="177" y="183.6" width="9" height="64.4"/>
        <rect class="col-light" x="192" y="180.8" width="9" height="67.2"/>
      </g>
      <g>
        <rect class="col-dark" x="27" y="232.6" width="6" height="15.4"/>
        <rect class="col-dark" x="42" y="229.8" width="6" height="18.2"/>
        <rect class="col-dark" x="57" y="215.8" width="6" height="32.2"/>
        <rect class="col-dark" x="73" y="203.2" width="6" height="44.8"/>
        <rect class="col-dark" x="88" y="203.2" width="6" height="44.8"/>
        <rect class="col-dark" x="104" y="227" width="6" height="21"/>
        <rect class="col-dark" x="119" y="200.4" width="6" height="47.6"/>
        <rect class="col-dark" x="134" y="197.6" width="6" height="50.4"/>
        <rect class="col-dark" x="150" y="211.6" width="6" height="36.4"/>
        <rect class="col-dark" x="165" y="227" width="6" height="21"/>
        <rect class="col-dark" x="181" y="218.6" width="6" height="29.4"/>
        <rect class="col-dark" x="196" y="215.8" width="6" height="32.2"/>
      </g>
      <g>
        <text class="cat" x="28" y="258">Text</text><text class="cat" x="43" y="258">Text</text>
        <text class="cat" x="58" y="258">Text</text><text class="cat" x="74" y="258">Text</text>
        <text class="cat" x="89" y="258">Text</text><text class="cat" x="105" y="258">Text</text>
        <text class="cat" x="120" y="258">Text</text><text class="cat" x="135" y="258">Text</text>
        <text class="cat" x="151" y="258">Text</text><text class="cat" x="166" y="258">Text</text>
        <text class="cat" x="182" y="258">Text</text><text class="cat" x="197" y="258">Text</text>
      </g>
    </symbol>
  </defs>
</svg>

<header class="headline-band">
  <h1 class="headline">Eight Color Schemes</h1>
</header>

<main>
  <section class="scheme dark-blue row-top col-1">
    <svg class="scheme-card" viewBox="0 0 214 274"><use href="#scheme-sheet"/></svg>
    <div class="scheme-name">Dark Blue</div>
  </section>
  <section class="scheme brown row-top col-2">
    <svg class="scheme-card" viewBox="0 0 214 274"><use href="#scheme-sheet"/></svg>
    <div class="scheme-name">Brown</div>
  </section>
  <section class="scheme blue row-top col-3">
    <svg class="scheme-card" viewBox="0 0 214 274"><use href="#scheme-sheet"/></svg>
    <div class="scheme-name">Blue</div>
  </section>
  <section class="scheme sea-green row-top col-4">
    <svg class="scheme-card" viewBox="0 0 214 274"><use href="#scheme-sheet"/></svg>
    <div class="scheme-name">Sea Green</div>
  </section>

  <section class="scheme grey row-bottom col-1">
    <svg class="scheme-card" viewBox="0 0 214 274"><use href="#scheme-sheet"/></svg>
    <div class="scheme-name">Grey</div>
  </section>
  <section class="scheme red row-bottom col-2">
    <svg class="scheme-card" viewBox="0 0 214 274"><use href="#scheme-sheet"/></svg>
    <div class="scheme-name">Red</div>
  </section>
  <section class="scheme green row-bottom col-3">
    <svg class="scheme-card" viewBox="0 0 214 274"><use href="#scheme-sheet"/></svg>
    <div class="scheme-name">Green</div>
  </section>
  <section class="scheme orange row-bottom col-4">
    <svg class="scheme-card" viewBox="0 0 214 274"><use href="#scheme-sheet"/></svg>
    <div class="scheme-name">Orange</div>
  </section>
</main>

</body>
</html>
```